business card design for luxurious real estate brand

using the attached logo, i am looking for a 2-sided business card design. the back should be the gold logo on black background. the front needs to include: gold logo, name, phone, email, and website

Industry/Entity Type

real estate

Contact Information for Business Card

logo, name, email, phone, website

Font styles to use
Sans Serif

```html
<!DOCTYPE html>
<html lang="en">
<head>
<meta charset="utf-8">
<title>Casa Ridgeway – Business Card</title>
<link href="https://fonts.googleapis.com/css2?family=Montserrat:wght@400;500;700&display=swap" rel="stylesheet">
<style>
  :root {
    --stage: #2b2b2c;
    --card: #1c1d1e;
    --gold: #ffcc00;
    --ink: #f2f2f2;
    --muted: #cfcfcf;
  }
  * { box-sizing: border-box; margin: 0; padding: 0; }
  html, body { width: 1200px; height: 900px; overflow: hidden; }
  body {
    background: var(--stage);
    font-family: "Montserrat", Arial, sans-serif;
    display: flex;
    flex-direction: column;
    align-items: center;
    justify-content: center;
    gap: 44px;
  }
  .card {
    width: 660px;
    height: 377px;
    background: var(--card);
    position: relative;
    box-shadow: 0 14px 30px rgba(0,0,0,.45);
  }
  .brand {
    display: flex;
    align-items: center;
    gap: 14px;
    color: var(--gold);
    font-weight: 500;
    text-transform: uppercase;
    letter-spacing: .32em;
  }
  .brand-mark {
    width: 16px; height: 16px;
    background: var(--gold);
    flex: none;
  }

  /* Front */
  .card-front .brand {
    position: absolute;
    top: 58px; left: 70px;
    font-size: 22px;
  }
  .person {
    position: absolute;
    top: 132px; left: 70px;
  }
  .person-name {
    color: var(--gold);
    font-weight: 700;
    font-size: 27px;
    line-height: 1.1;
  }
  .person-title {
    color: var(--ink);
    font-size: 14px;
    margin-top: 4px;
  }
  .contact-list {
    list-style: none;
    margin-top: 18px;
    display: grid;
    gap: 7px;
  }
  .contact-item {
    display: flex;
    align-items: center;
    gap: 10px;
    color: var(--ink);
    font-size: 14px;
  }
  .contact-icon { width: 13px; height: 13px; fill: var(--gold); flex: none; }
  .divider {
    position: absolute;
    left: 70px; right: 70px; top: 292px;
    height: 1.5px;
    background: var(--gold);
  }
  .address {
    position: absolute;
    right: 70px; top: 306px;
    text-align: right;
    color: var(--ink);
    font-size: 13px;
    line-height: 1.45;
  }

  /* Back */
  .card-back {
    display: flex;
    align-items: center;
    justify-content: center;
  }
  .card-back .brand { font-size: 34px; gap: 20px; }
  .card-back .brand-mark { width: 24px; height: 24px; }
</style>
</head>
<body>

  <section class="card card-front" aria-label="Business card front">
    <div class="brand"><span class="brand-mark"></span>Casa Ridgeway</div>

    <div class="person">
      <p class="person-name">Daniel Harper</p>
      <p class="person-title">CEO &amp; Founder</p>
      <ul class="contact-list">
        <li class="contact-item">
          <svg class="contact-icon" viewBox="0 0 24 24" aria-hidden="true"><path d="M6.6 10.8a15.1 15.1 0 0 0 6.6 6.6l2.2-2.2a1 1 0 0 1 1-.25 11.4 11.4 0 0 0 3.6.57 1 1 0 0 1 1 1V20a1 1 0 0 1-1 1A17 17 0 0 1 3 4a1 1 0 0 1 1-1h3.5a1 1 0 0 1 1 1c0 1.25.2 2.45.57 3.57a1 1 0 0 1-.25 1z"/></svg>
          215-555-0148
        </li>
        <li class="contact-item">
          <svg class="contact-icon" viewBox="0 0 24 24" aria-hidden="true"><path d="M2 5h20v14H2z M3.5 6.5 12 13l8.5-6.5" fill="none" stroke="#ffcc00" stroke-width="2"/></svg>
          info@casaridgeway.com
        </li>
        <li class="contact-item">
          <svg class="contact-icon" viewBox="0 0 24 24" aria-hidden="true"><circle cx="12" cy="12" r="9" fill="none" stroke="#ffcc00" stroke-width="2"/><path d="M3 12h18M12 3c3 3.2 3 14.8 0 18M12 3c-3 3.2-3 14.8 0 18" fill="none" stroke="#ffcc00" stroke-width="1.6"/></svg>
          www.casaridgeway.com
        </li>
      </ul>
    </div>

    <div class="divider"></div>

    <address class="address" style="font-style:normal">
      48 Meridian Lane, Suite 210<br>
      Lansdale, PA 19446
    </address>
  </section>

  <section class="card card-back" aria-label="Business card back">
    <div class="brand"><span class="brand-mark"></span>Casa Ridgeway</div>
  </section>

</body>
</html>
```